Velmora Water Purification

We need a website set up on a "Free account" WordPress platform. (This is the type of Wordpress site that you can sign up for and create online for free (not a server-hosted type.)
The website will be for a water purification company. They install devices in homes to purify the water for safer drinking, bathing, and cleaning.
Our logo is attached. Please keep color scheme of the website consistent with the logo.
Water Purification

```html
<!DOCTYPE html>
<html lang="en">
<head>
<meta charset="utf-8">
<title>Velmora Water Purification</title>
<link href="https://fonts.googleapis.com/css2?family=Open+Sans:wght@300;400;600;700&display=swap" rel="stylesheet">
<style>
:root{
  --canvas:#fbf9f8;
  --page:#f4f2f1;
  --nav:#2d2b2f;
  --footer:#2b2a2e;
  --indigo:#5e6db1;
  --rose:#d13f6c;
  --heading:#737a82;
  --body:#8d9298;
  --white:#ffffff;
  --footer-text:#a4a4a8;
  --footer-head:#8a8a8e;
}
*{margin:0;padding:0;box-sizing:border-box}
html,body{width:1200px;height:1200px;overflow:hidden;background:var(--canvas);font-family:"Open Sans",Arial,sans-serif}
.site{position:absolute;left:337px;top:63px;width:591px;height:1073px;background:var(--page);box-shadow:0 24px 50px rgba(60,40,40,.28);overflow:hidden}
.abs{position:absolute}

/* nav */
.nav{left:0;top:0;width:591px;height:35px;background:var(--nav);z-index:2}
.brand{left:36px;top:10px;display:flex;align-items:center;gap:5px;color:var(--white);font-size:10px;font-weight:600}
.brand-dot{width:12px;height:12px;border-radius:50%;background:var(--indigo)}
.nav-link{top:12px;color:var(--white);font-size:8px;font-weight:700;letter-spacing:.2px;white-space:nowrap}

/* hero */
.hero{left:0;top:35px;width:591px;height:359px;background:radial-gradient(ellipse at 80% 40%,#9aa0aa 0%,#5d6068 30%,#2f3036 70%,#1e1f24 100%)}
.hero-badge{left:59px;top:89px;width:236px;height:236px;border-radius:50%;background:rgba(80,92,150,.82);color:var(--white);text-align:center}
.hero-kicker{position:absolute;top:60px;width:100%;font-size:13px;font-weight:700;letter-spacing:.3px}
.hero-title{position:absolute;top:74px;width:100%;font-size:29px;font-weight:300;letter-spacing:.5px}
.hero-copy{position:absolute;top:118px;left:24px;width:190px;font-size:11px;line-height:13.8px;font-weight:300}
.dots{left:285px;top:361px;display:flex;gap:3px;align-items:center}
.dot{width:7px;height:7px;border-radius:50%;background:var(--white)}
.dot.active{width:29px;border-radius:4px}

/* products */
.prod-title{font-size:27px;font-weight:600;color:var(--heading);white-space:nowrap}
.prod-copy{font-size:11px;line-height:13.7px;font-weight:300;color:var(--body);width:190px}
.btn{height:18px;border-radius:6px;color:var(--white);font-size:10px;font-weight:600;text-align:center;line-height:18px}
.btn-indigo{background:var(--indigo)}
.btn-rose{background:var(--rose)}
.disc{border-radius:50%}
.placeholder{border-radius:8px}

/* features */
.features{left:0;top:841px;width:591px;height:48px;background:var(--white)}
.feat-title{font-size:10px;color:#6b6f75;font-weight:400}
.feat-copy{font-size:5.5px;line-height:7px;color:#9a9ea3;width:150px}

/* footer */
.footer{left:0;top:889px;width:591px;height:184px;background:var(--footer)}
.foot-head{top:29px;font-size:7.5px;color:var(--footer-head);letter-spacing:.3px}
.foot-list{top:54px;list-style:none;font-size:7.5px;color:var(--footer-text);line-height:14.6px}
.social{top:132px;left:454px;display:flex;gap:8px}
.social span{width:17px;height:17px;border:1px solid #9a9a9e;border-radius:50%}
.legal{top:152px;right:37px;font-size:7.5px;color:#d2d2d6;white-space:nowrap}
</style>
</head>
<body>
<main class="site">
  <header class="nav abs">
    <div class="brand abs"><span class="brand-dot"></span>Velmora</div>
    <span class="nav-link abs" style="left:131px">WATER PURIFIERS</span>
    <span class="nav-link abs" style="left:238px">AIR PURIFIERS</span>
    <span class="nav-link abs" style="left:330px">VACUUM CLEANERS</span>
    <span class="nav-link abs" style="left:441px">ABOUT US</span>
    <span class="nav-link abs" style="left:514px">CONTACT US</span>
  </header>

  <section class="hero abs" role="img" aria-label="Photo of water pouring from pipes with soft bokeh droplets">
    <div class="hero-badge abs">
      <div class="hero-kicker">VELMORA WATER</div>
      <div class="hero-title">PURIFICATION</div>
      <p class="hero-copy">Lorem ipsum dolor sit amet, consec-tetuer adipiscing elit, sed diam nonummy nibh euismod tincidunt ut laoreet dolore magna aliquam erat</p>
    </div>
    <div class="dots abs"><span class="dot"></span><span class="dot active"></span><span class="dot"></span><span class="dot"></span></div>
  </section>

  <h2 class="prod-title abs" style="left:118px;top:434px">Water Purifiers</h2>
  <p class="prod-copy abs" style="left:118px;top:478px">Lorem ipsum dolor sit amet, consec-tetuer adipiscing elit, sed diam nonummy nibh euismod tincidunt ut laoreet dolore magna aliquam erat volutpat. Ut wisi</p>
  <div class="btn btn-indigo abs" style="left:118px;top:560px;width:103px">VIEW</div>
  <div class="disc abs" style="left:372px;top:446px;width:122px;height:122px;background:var(--indigo)"></div>
  <div class="placeholder abs" role="img" aria-label="White wall-mounted water purifier unit" style="left:405px;top:463px;width:56px;height:92px;background:linear-gradient(90deg,#e4e6ea,#fafafa)"></div>

  <div class="disc abs" style="left:137px;top:639px;width:116px;height:116px;background:var(--rose)"></div>
  <div class="placeholder abs" role="img" aria-label="White air purifier with pink floral print" style="left:151px;top:670px;width:80px;height:114px;background:linear-gradient(90deg,#eceaec,#fbfafa)"></div>
  <h2 class="prod-title abs" style="right:68px;top:646px">Air Purifiers</h2>
  <p class="prod-copy abs" style="right:68px;top:690px;text-align:right">Lorem ipsum dolor sit amet, consec-tetuer adipiscing elit, sed diam nonummy nibh euismod tincidunt ut laoreet dolore magna aliquam erat volutpat. Ut wisi</p>
  <div class="btn btn-rose abs" style="left:424px;top:775px;width:103px">VIEW</div>

  <section class="features abs">
    <div class="abs" style="left:35px;top:5px">
      <div class="feat-title">Advantage</div>
      <p class="feat-copy">Lorem ipsum dolor sit amet, consectetuer adipiscing elit, sed diam nonummy nibh euismod tincidunt ut laoreet dolore magna aliquam erat volutpat. Ut wisi</p>
    </div>
    <div class="abs" style="left:237px;top:9px">
      <div class="feat-title">Most Certified &amp; Awarded</div>
      <p class="feat-copy">Lorem ipsum dolor sit amet, consectetuer adipiscing elit, sed diam nonummy nibh euismod tincidunt ut</p>
    </div>
    <div class="abs" style="left:433px;top:9px">
      <div class="feat-title">Trusted By MILLIONS</div>
      <p class="feat-copy" style="width:125px">Lorem ipsum dolor sit amet, consectetuer adipiscing elit, sed diam nonummy nibh</p>
    </div>
  </section>

  <footer class="footer abs">
    <div class="foot-head abs" style="left:32px">ADVANTAGE</div>
    <ul class="foot-list abs" style="left:32px"><li>Water Purifiers</li><li>Air Purifiers</li><li>Water softeners</li><li>Cooking Appliance</li><li>Vaccum Cleaners</li></ul>
    <div class="foot-head abs" style="left:180px">COMPANY</div>
    <ul class="foot-list abs" style="left:180px"><li>Overview</li><li>Awards &amp; recgnitions</li><li>Certification</li><li>Become a Trade partner</li></ul>
    <div class="foot-head abs" style="left:333px">SUPPORT</div>
    <ul class="foot-list abs" style="left:333px"><li>customer Service</li><li>Where to buy</li><li>Press Kit</li><li>Offices</li><li>Careers</li></ul>
    <div class="foot-head abs" style="left:464px">BUY NOW</div>
    <ul class="foot-list abs" style="left:464px"><li>Online Store</li><li>Terms &amp; Condition</li><li>Return &amp; Refund Policy</li><li>Billing &amp; Shipping</li></ul>
    <div class="social abs"><span></span><span></span><span></span><span></span></div>
    <div class="legal abs">Disclaimer / &nbsp;Privacy Policy &nbsp;/ &nbsp;Blog &nbsp;/ &nbsp;Site Map</div>
  </footer>
</main>
</body>
</html>
```